design a company brochure

tri-fold brochure. reference website: orvanta.llc for information (website under construction but should have the basic information)

Target Market(s)

Users of sign Language interpreting services; businesses, community, hospitals, schools, colleges, medical, religious, and legal settings

Industry/Entity Type

Community Service

Font styles to use
Serif
Decorative

Colors
734ea0
9ccb3b

Requirements
Must have
• Brochure should be worded so it applies to the above markets and focuses on our professionalism, integrity in business
Nice to have
• I would like the designers to look at the business website under construction (orvanta.llc) or an older website (orvanta-tquel.com). Company was restructured and is now just ORVA, LLC.
A darker green than what is shown here. Again, reference the website
Should not have
• No personal pictures in the brochure - can use clip art or interpreter/interpreting shots.

```html
<!DOCTYPE html>
<html lang="en">
<head>
<meta charset="utf-8">
<title>ORVA, LLC – Educational &amp; Medical Sign Language Interpreters Brochure</title>
<link href="https://fonts.googleapis.com/css2?family=Crimson+Text:wght@400;600;700&display=swap" rel="stylesheet">
<style>
  :root{
    --purple:#8e1c72;
    --purple-deep:#734ea0;
    --magenta:#a3206f;
    --green:#5f8f25;
    --green-light:#9ccb3b;
    --ink:#2b2b2b;
    --muted:#555;
    --paper:#ffffff;
    --bg:#efefef;
  }
  *{box-sizing:border-box;margin:0;padding:0}
  html,body{width:1200px;height:2297px;overflow:hidden;background:var(--bg)}
  body{position:relative;font-family:"Crimson Text",Georgia,serif;color:var(--ink)}
  .spread{position:absolute;left:204px;width:792px;height:560px;background:var(--paper);box-shadow:0 2px 6px rgba(0,0,0,.18);overflow:hidden}
  .spread--outside{top:1038px}
  .spread--inside{top:1656px}
  .panel{position:absolute;top:0;width:264px;height:560px}
  .panel--1{left:0}.panel--2{left:264px}.panel--3{left:528px}
  .tab-heading{position:relative;height:19px;margin-bottom:6px}
  .tab-heading span{display:inline-block;height:19px;line-height:20px;padding:0 22px 0 6px;background:var(--purple);color:#fff;font-weight:700;font-size:14px;letter-spacing:.5px;clip-path:polygon(0 0,88% 0,100% 100%,0 100%)}
  .tab-heading::after{content:"";position:absolute;left:0;right:0;bottom:0;border-bottom:1px solid var(--purple)}
  .content{position:absolute;left:29px;width:205px;top:28px}
  p.body{font-size:6.6px;line-height:1.4;color:var(--ink)}
  .q{font-size:6.6px;font-weight:700;color:var(--green);text-transform:uppercase;line-height:1.3;margin:12px 0 5px;letter-spacing:.2px}
  .brand-text{font-weight:600;color:var(--ink);letter-spacing:.5px}
  .brand-row{display:flex;gap:16px;margin:20px 0 6px;font-size:9px}
  .brand-row .brand-text::before{content:"";display:inline-block;width:8px;height:8px;border:1px solid var(--ink);margin-right:4px;vertical-align:-1px}
  .lead-title{font-size:14.5px;line-height:1.1}
  .lead-sub{font-size:9px;margin-bottom:12px}
  .img-box{position:absolute}
  .pill{display:block;margin:0 auto;width:134px;height:22px;line-height:22px;border-radius:11px;background:var(--purple);color:#fff;font-weight:700;font-size:14px;text-align:center;letter-spacing:.5px}
  .person{display:flex;gap:12px;margin-top:20px;padding-left:28px}
  .person .photo{flex:none;width:52px;height:52px;border-radius:50%;border:2px solid var(--green);background:radial-gradient(circle at 50% 45%,#b59684,#5a4a44)}
  .person h3{font-size:10px;font-weight:400;color:var(--purple)}
  .person .role{font-size:6.8px;margin-bottom:5px}
  .person p{font-size:6.3px;line-height:1.4;width:115px}
  .cta-row{display:flex;justify-content:center;align-items:center;gap:18px;margin-top:30px;font-size:8px}
  .request-btn{background:var(--green);color:#fff;border-radius:14px;padding:4px 10px;font-size:6.5px;line-height:1.1;text-align:center}
  .contact{text-align:center;font-size:8.4px;line-height:1.35}
  .contact svg{display:block;margin:6px auto 2px;width:9px;height:9px;fill:var(--ink)}
  .web{position:absolute;bottom:18px;left:0;right:0;text-align:center;font-size:11px}
  .web b{font-weight:400;color:var(--purple)}
  .hero-title{position:absolute;left:30px;top:296px;color:#fff}
  .hero-title h1{font-size:36px;font-weight:700;line-height:1;letter-spacing:.3px}
  .hero-title h2{font-size:32px;font-weight:400;line-height:1.1}
  .hero-title hr{width:24px;border:0;border-top:1.5px solid #fff;margin:10px 0}
  .hero-title p{font-size:14.5px}
  .hero-brand{position:absolute;top:462px;left:0;right:0;text-align:center;font-size:16px}
  .hero-brand::before{content:"";display:inline-block;width:14px;height:14px;border:1.5px solid var(--ink);margin-right:6px;vertical-align:-2px}
  .service{margin-top:14px}
  .service h4{display:flex;align-items:center;gap:10px;font-size:10.5px;font-weight:600;color:var(--green);letter-spacing:.6px;margin-bottom:4px}
  .service h4 svg{width:18px;height:18px;stroke:var(--purple);fill:none;stroke-width:1.3}
  .service ul{list-style:none;padding-left:35px}
  .service li{font-size:7.2px;line-height:1.1;margin-bottom:6px;position:relative;padding-left:13px}
  .service li::before{content:"";position:absolute;left:0;top:1px;width:7px;height:7px;border-radius:50%;background:var(--green)}
  .service li::after{content:"";position:absolute;left:2px;top:2.4px;width:2.5px;height:1.5px;border-left:1px solid #fff;border-bottom:1px solid #fff;transform:rotate(-45deg)}
</style>
</head>
<body>

<!-- Outside spread -->
<section class="spread spread--outside">
  <div class="panel panel--1">
    <div class="content">
      <div class="tab-heading"><span>CAREERS</span></div>
      <p class="body">Whether you prefer K-12 educational settings or working with adults we have a need for you. If you are passionate about your job and want to work with a company that exudes the highest professional standards, please contact us.</p>
      <div class="brand-row"><span class="brand-text">ORVA, LLC</span><span class="brand-text">ORVA, LLC</span></div>
      <div class="lead-title">Educational and Medical</div>
      <div class="lead-sub">Sign Language Interpreters</div>
      <div class="tab-heading"><span>RESOURCES</span></div>
      <div class="q">Resources when do I need to<br>request an interpreter</div>
      <p class="body">Sign language interpreters are needed when you communicate with a deaf individual whose primary source of communication is sign language. Always ask the deaf person first if an interpreter is needed.</p>
      <div class="q">Rights of deaf and hard of<br>hearing/ADA</div>
      <p class="body">The Americans with Disability Act (ADA) is a law that prohibits discrimination against people with disabilities including deaf and hard of hearing individuals. All businesses and government agencies are required to provide effective communication.</p>
      <div class="q">Benefits to small<br>businesses</div>
      <p class="body">Small businesses may qualify for a tax credit under Section 44 of the Internal Revenue Code. This tax incentive was created in 1990 to help small businesses cover ADA related expenses.</p>
    </div>
    <div class="img-box" role="img" aria-label="Letter block beside a hand forming a fingerspelled letter" style="left:36px;top:455px;width:200px;height:105px;background:linear-gradient(90deg,#fff 0%,#f2e1dc 55%,#e8cfc4 80%,#fff 100%)"></div>
  </div>

  <div class="panel panel--2">
    <div style="position:absolute;top:28px;left:0;right:0">
      <div class="pill">ABOUT US</div>
      <div class="person">
        <div class="photo" role="img" aria-label="Portrait photo of the owner"></div>
        <div>
          <h3>Dana Whitfield</h3>
          <div class="role">Owner</div>
          <p>Dana Whitfield is a native of Nebraska but has lived in Colorado long enough to call it home. She graduated in 1998 from Foothill Valley Community College with an A.A.S.</p>
        </div>
      </div>
      <div class="person">
        <div class="photo" role="img" aria-label="Portrait photo of the staffing coordinator"></div>
        <div>
          <h3>Lena Marsh</h3>
          <div class="role">Staffing Coordinator</div>
          <p>Recognizing the great need for qualified interpreters in the public education system, she partnered with Lena Marsh to offer school</p>
        </div>
      </div>
      <div class="cta-row"><span class="brand-text">ORVA, LLC</span><span class="request-btn">Request an<br>Interpreter</span></div>
      <div class="pill" style="margin-top:30px">CONTACT US</div>
      <div class="contact" style="margin-top:10px">
        <div>ORVA / TQUEL, LLC</div>
        <svg viewBox="0 0 24 24"><path d="M6.6 10.8a15.2 15.2 0 0 0 6.6 6.6l2.2-2.2a1 1 0 0 1 1-.24 11.4 11.4 0 0 0 3.6.57 1 1 0 0 1 1 1V20a1 1 0 0 1-1 1A17 17 0 0 1 3 4a1 1 0 0 1 1-1h3.5a1 1 0 0 1 1 1c0 1.25.2 2.45.57 3.57a1 1 0 0 1-.25 1z"/></svg>
        <div>(720) 555-0148</div>
        <svg viewBox="0 0 24 24"><path d="M6 2h9v5H6zM4 8h16v10H4zm3 2v2h10v-2zM6 19h12v3H6z"/></svg>
        <div>(303) 555-0193</div>
        <svg viewBox="0 0 24 24"><path d="M2 5h20v14H2zm2 2v.5l8 5 8-5V7z"/></svg>
        <div>info@orvanta-tquel.com</div>
        <svg viewBox="0 0 24 24"><path d="M11 2h2v3h6l2 2-2 2h-6v2h-7l-2-2 2-2h5V5H5V3h6zm0 11h2v9h-2z"/></svg>
        <div>PO BOX 40718<br>Denver, Colorado 80202</div>
      </div>
    </div>
    <div class="web">www.<b>orvanta-tquel</b>.com</div>
  </div>

  <div class="panel panel--3">
    <svg width="264" height="560" viewBox="0 0 264 560" style="position:absolute;left:0;top:0">
      <defs>
        <linearGradient id="heroPhoto" x1="0" y1="0" x2="1" y2="1"><stop offset="0" stop-color="#8d8a80"/><stop offset=".5" stop-color="#cdb8a8"/><stop offset="1" stop-color="#e9e4df"/></linearGradient>
        <linearGradient id="heroBand" x1="0" y1="0" x2="1" y2="1"><stop offset="0" stop-color="#a3206f"/><stop offset="1" stop-color="#7a2a90"/></linearGradient>
      </defs>
      <rect width="264" height="262" fill="url(#heroPhoto)" role="img" aria-label="Photo of an interpreter signing with her hands"/>
      <polygon points="0,260 264,232 264,432 0,446" fill="url(#heroBand)"/>
      <polygon points="0,446 264,426 264,438 0,453" fill="var(--green)"/>
    </svg>
    <div class="hero-title">
      <h1>Educational</h1>
      <h2>&amp; Medical</h2>
      <hr>
      <p>Sign Language Interpreters</p>
    </div>
    <div class="hero-brand brand-text">ORVA, LLC</div>
    <div class="web">www.<b>orvanta-tquel</b>.com</div>
  </div>
</section>

<!-- Inside spread -->
<section class="spread spread--inside">
  <div class="panel panel--1">
    <div class="content">
      <div class="tab-heading"><span>FAQ'S</span></div>
      <div class="q">Can the deaf person bring in their<br>own interpreter?</div>
      <p class="body">It is not recommended. Professional interpreters are trained and must abide by NIRA's professional Code of Conduct. This will ensure message accuracy, impartiality and confidentiality.</p>
      <div class="q">Is there always a two<br>hour minimum?</div>
      <p class="body">Many assignments require a two hour minimum however we are more than happy to come up with an agreement that fits your needs.</p>
      <div class="q">Do you only supply educational<br>interpreters?</div>
      <p class="body">Although our main focus is educational interpreting, we do provide services for medical and community interpreting as well.</p>
      <div style="text-align:right;margin-top:22px;font-size:11px" class="brand-text">ORVA, LLC</div>
    </div>
    <svg width="264" height="560" viewBox="0 0 264 560" style="position:absolute;left:0;top:0">
      <defs><linearGradient id="faqPhoto" x1="0" y1="0" x2="1" y2="1"><stop offset="0" stop-color="#d9b8a6"/><stop offset=".6" stop-color="#c97aa8"/><stop offset="1" stop-color="#b8508f"/></linearGradient></defs>
      <polygon points="0,243 264,308 264,560 0,560" fill="url(#faqPhoto)" role="img" aria-label="Photo of hands signing, tinted pink"/>
      <polygon points="0,243 264,308 264,316 0,252" fill="var(--purple)"/>
      <polygon points="264,290 264,420 150,352" fill="#d687b6" opacity=".85"/>
    </svg>
  </div>

  <div class="panel panel--2">
    <div class="content" style="width:210px">
      <div class="tab-heading"><span>OUR SERVICES</span></div>
      <div class="service">
        <h4><svg viewBox="0 0 20 20"><circle cx="10" cy="6" r="4"/><path d="M3 19c0-5 3-7 7-7s7 2 7 7"/></svg>EDUCATIONAL</h4>
        <ul><li>K-12 Settings</li><li>Post-Secondary</li><li>Parent/Teacher Conference</li><li>IEP Meetings</li><li>Staff Meetings</li><li>Extracurricular Activities</li></ul>
      </div>
      <div class="service">
        <h4><svg viewBox="0 0 20 20"><path d="M10 16S3 11 3 7a3.5 3.5 0 0 1 7-1 3.5 3.5 0 0 1 7 1c0 4-7 9-7 9z"/></svg>MEDICAL</h4>
        <ul><li>Doctor's Appointments</li><li>ER Visits</li><li>Patient Education and Counseling</li><li>Pre-Op/Post-Op Appointments</li><li>Physical, Speech &amp; Occupational Therapy</li></ul>
      </div>
      <div class="service">
        <h4><svg viewBox="0 0 20 20"><path d="M1 8l4-3 5 3 5-3 4 3M4 9l5 5 2-1 4-4"/></svg>BUSINESS</h4>
        <ul><li>Staff Meetings</li><li>Interviews &amp; Orientations</li><li>Conferences</li><li>Job Training</li></ul>
      </div>
    </div>
  </div>

  <div class="panel panel--3">
    <svg width="264" height="240" viewBox="0 0 264 240" style="position:absolute;left:0;top:0">
      <defs><linearGradient id="childPhoto" x1="0" y1="0" x2="1" y2="1"><stop offset="0" stop-color="#9a9a9a"/><stop offset=".5" stop-color="#6f86a8"/><stop offset="1" stop-color="#c9c7c4"/></linearGradient></defs>
      <polygon points="0,0 264,0 264,226 0,212" fill="url(#childPhoto)" role="img" aria-label="Photo of a smiling child signing"/>
      <polygon points="0,212 264,226 264,234 0,219" fill="var(--purple)"/>
    </svg>
    <div class="content" style="top:250px">
      <div class="service">
        <h4><svg viewBox="0 0 20 20"><path d="M10 2l2.4 5 5.4.6-4 3.7 1.1 5.3L10 14l-4.9 2.6 1.1-5.3-4-3.7 5.4-.6z"/></svg>SPECIAL OCCASIONS</h4>
        <ul><li>Weddings</li><li>Funerals</li><li>Graduations</li></ul>
      </div>
      <div class="service">
        <h4><svg viewBox="0 0 20 20"><path d="M10 2v12M10 4l-4 8v6M10 4l4 8v6"/></svg>RELIGIOUS</h4>
        <ul><li>Church Services &amp; Sermons</li><li>Counseling</li><li>Religious Ceremonies</li></ul>
      </div>
    </div>
  </div>

  <div class="img-box" role="img" aria-label="Row of hands fingerspelling letters" style="left:290px;top:418px;width:490px;height:138px;background:linear-gradient(180deg,#fff 0%,#f3dfd3 45%,#e9c8b6 100%)"></div>
  <div style="position:absolute;left:264px;right:0;bottom:0;height:4px;background:var(--purple)"></div>
</section>

</body>
</html>
```